3 signs to go on a trailer

due to logo change we need to update our trailer design signage the trailer has 3 panels 2 panels @ 650mmx1200 1@500mmx1200, i have attached a sample i was working on please feel free to change anything you feel needs change. im trying to achive a simple and soft design. i also uploaded our new logo in AI file, please feel free to contact me for further information. also a sketch of how the trailer looks like

```html
<!DOCTYPE html>
<html lang="en">
<head>
<meta charset="utf-8">
<title>Integrated Services – Trailer Panel</title>
<link rel="stylesheet" href="https://fonts.googleapis.com/css2?family=Arimo:wght@400;700&display=swap">
<style>
  :root {
    --green-deep: #10763f;
    --green-soft: #83c77d;
    --ink: #111111;
    --grey-mark: #58595b;
    --paper: #ffffff;
  }
  html, body {
    margin: 0;
    padding: 0;
    width: 1200px;
    height: 2400px;
    overflow: hidden;
    background: var(--paper);
  }
  .panel {
    position: relative;
    width: 1200px;
    height: 2400px;
    overflow: hidden;
    background: var(--paper);
    font-family: "Arimo", Arial, sans-serif;
  }
  .panel-shapes {
    position: absolute;
    inset: 0;
    width: 1200px;
    height: 2400px;
  }
  .shape-deep { fill: var(--green-deep); }
  .shape-soft { fill: var(--green-soft); }
  .service-block {
    position: absolute;
    right: 40px;
    top: 1576px;
    text-align: right;
    color: var(--ink);
  }
  .service-title {
    margin: 0;
    font-weight: 700;
    font-size: 66px;
    line-height: 1;
    letter-spacing: 0.5px;
  }
  .service-list {
    list-style: none;
    margin: 12px 0 0;
    padding: 0;
    font-weight: 400;
    font-size: 44px;
    line-height: 59px;
  }
  .brand {
    position: absolute;
    right: 40px;
    bottom: 150px;
    display: flex;
    align-items: center;
    gap: 28px;
    color: var(--grey-mark);
    font-weight: 700;
    font-size: 60px;
    line-height: 1;
  }
  .brand-dot {
    width: 90px;
    height: 90px;
    border-radius: 50%;
    background: var(--grey-mark);
  }
</style>
</head>
<body>
  <main class="panel">
    <svg class="panel-shapes" viewBox="0 0 1200 2400" aria-hidden="true">
      <polygon class="shape-deep" points="0,0 1218,0 0,1552"/>
      <path class="shape-soft" d="M1200,24 L552,928 Q900,944 1200,736 Z"/>
    </svg>

    <section class="service-block">
      <h1 class="service-title">INTEGRATED SERVICES</h1>
      <ul class="service-list">
        <li>Cleaning</li>
        <li>Security</li>
        <li>Maintenance</li>
      </ul>
    </section>

    <div class="brand">
      <span class="brand-dot"></span>
      <span class="brand-name">Verdant Facility Group</span>
    </div>
  </main>
</body>
</html>
```